Pinegate Health group for a medical office

We need a website created that for our new medical office that will support online booking for appointments. You designed the logo already.

```html
<!DOCTYPE html>
<html lang="en">
<head>
<meta charset="utf-8">
<title>Pinegate Health Group</title>
<link rel="stylesheet" href="https://fonts.googleapis.com/css2?family=Montserrat:wght@600;700&family=Roboto:ital,wght@0,400;0,500;0,700;1,400&display=swap">
<style>
:root{
  --accent:#d4906a;
  --accent-soft:#f7ece5;
  --blue:#29a8e0;
  --navy:#1b2e4c;
  --ink:#1e2a3a;
  --body:#333a44;
  --muted:#8a93a0;
  --grey-bg:#f4f4f4;
  --line:#dcdfe3;
  --white:#ffffff;
}
*{box-sizing:border-box;margin:0;padding:0}
html,body{width:1200px;height:4410px;overflow:hidden}
body{position:relative;font-family:"Roboto",Arial,sans-serif;color:var(--body);background:var(--white)}
.abs{position:absolute}
.btn{position:absolute;display:flex;align-items:center;justify-content:center;background:var(--accent);color:var(--white);font:500 15px "Roboto",Arial,sans-serif;letter-spacing:.3px;text-transform:uppercase}
.btn-ghost{background:var(--accent-soft);color:var(--accent)}
.heading{font-family:"Montserrat",Arial,sans-serif;font-weight:700;color:var(--ink);text-transform:uppercase}
.heading .hl{color:var(--blue)}
.rule{position:absolute;height:3px;background:var(--accent)}

/* header */
.site-header{position:absolute;left:0;top:0;width:1200px;height:122px;background:var(--white)}
.brand{position:absolute;left:111px;top:26px;font:700 28px/35px "Montserrat",Arial,sans-serif;color:var(--navy);text-transform:uppercase}
.header-phone{position:absolute;left:660px;top:29px;display:flex;align-items:center;gap:10px;font:500 18px "Roboto",Arial,sans-serif;color:var(--ink)}
.main-nav{position:absolute;right:111px;top:88px;display:flex;gap:31px;font:500 15px "Roboto",Arial,sans-serif;color:var(--ink);text-transform:uppercase}
.main-nav .active{color:var(--accent)}

/* hero */
.hero{position:absolute;left:0;top:122px;width:1200px;height:600px;background:linear-gradient(100deg,#dbe7ef 0%,#e9f1f6 45%,#c9dce8 70%,#aec8da 100%)}
.hero-title{position:absolute;left:0;width:1200px;top:178px;text-align:center;font:700 40px/46px "Montserrat",Arial,sans-serif;color:var(--navy);text-transform:uppercase}
.hero-text{position:absolute;left:0;width:1200px;top:284px;text-align:center;font:400 19px/30px "Roboto",Arial,sans-serif;color:var(--ink)}
.dots{position:absolute;left:572px;top:562px;display:flex;gap:7px}
.dots span{width:14px;height:14px;border-radius:50%;border:2px solid var(--navy)}
.dots .on{background:var(--navy)}

/* about */
.about-text p{font:400 14px/24px "Roboto",Arial,sans-serif;color:var(--body);text-align:justify;margin-bottom:12px}

/* services */
.services{position:absolute;left:0;top:1400px;width:1200px;height:720px;background:var(--grey-bg)}
.card{position:absolute;top:177px;width:308px;background:var(--white);border-radius:10px;box-shadow:0 3px 10px rgba(0,0,0,.12);padding:5px}
.card-photo{height:210px;border-radius:8px 8px 0 0}
.card-icon{position:absolute;left:116px;top:174px;width:76px;height:76px;border-radius:50%;display:flex;align-items:center;justify-content:center}
.card h3{margin-top:48px;text-align:center;font:700 16px/23px "Roboto",Arial,sans-serif;color:var(--ink);text-transform:uppercase}
.card p{margin-top:4px;text-align:center;font:400 15px/23px "Roboto",Arial,sans-serif;color:var(--body);padding:0 22px}
.card .btn{position:static;width:146px;height:44px;margin:18px auto 26px}
.arrow{position:absolute}

/* booking */
.book-box{position:absolute;left:584px;top:2232px;width:616px;height:531px;background:var(--blue);color:var(--white)}
.book-box p{font:400 14px/24px "Roboto",Arial,sans-serif;margin-bottom:12px}

/* testimonials */
.quote-card{position:absolute;left:293px;top:2945px;width:714px;height:296px;background:var(--white);box-shadow:0 2px 14px rgba(0,0,0,.09)}
.round-btn{position:absolute;width:36px;height:36px;border-radius:50%;display:flex;align-items:center;justify-content:center}

/* contact */
.contact{position:absolute;left:0;top:3350px;width:1200px;height:696px;background:var(--grey-bg)}
.info{position:absolute;top:152px;display:flex;gap:16px}
.info b{display:block;font:500 15px "Roboto",Arial,sans-serif;color:var(--ink);text-transform:uppercase}
.info span{font:400 13px/17px "Roboto",Arial,sans-serif;color:var(--muted)}
.field-label{position:absolute;font:400 16px "Roboto",Arial,sans-serif;color:var(--ink)}
.field{position:absolute;height:45px;background:var(--white);border:1px solid var(--line);padding:14px 18px;font:italic 400 13px "Roboto",Arial,sans-serif;color:#a3a9b1}

/* footer */
.site-footer{position:absolute;left:0;top:4046px;width:1200px;height:364px;background:var(--navy);color:var(--white)}
.site-footer h4{position:absolute;top:58px;font:700 15px "Roboto",Arial,sans-serif;text-transform:uppercase}
.site-footer h4::after{content:"";position:absolute;left:0;top:27px;width:46px;height:2px;background:var(--accent)}
.foot-item{position:absolute;left:371px;display:flex;gap:18px;font:400 14px/23px "Roboto",Arial,sans-serif}
.foot-item i{width:38px;height:38px;border-radius:50%;background:var(--white);display:flex;align-items:center;justify-content:center;flex:none}
.quick{position:absolute;left:659px;top:110px;list-style:none;font:400 14px/29px "Roboto",Arial,sans-serif}
.social{position:absolute;left:829px;top:205px;display:flex;gap:8px}
.social span{width:37px;height:37px;border-radius:50%;border:1.5px solid var(--white)}
.social .on{background:var(--accent);border-color:var(--accent)}
</style>
</head>
<body>

<header class="site-header">
  <div class="brand">Pinegate<br>Health Group</div>
  <div class="header-phone">
    <svg width="16" height="16" viewBox="0 0 16 16"><rect width="16" height="16" rx="3" fill="#29a8e0"/><path d="M5 3.5l2 2-1 1.3c.6 1.3 1.6 2.3 2.9 2.9l1.3-1 2 2-1.2 1.6C7.5 12 4 8.5 3.7 4.7z" fill="#fff"/></svg>
    +1 (555) 014 2200
  </div>
  <div class="btn" style="left:866px;top:17px;width:223px;height:48px">Book an Appointment</div>
  <nav class="main-nav">
    <span class="active">Home</span><span>About Us</span><span>Services</span><span>Providers</span><span>Patient Resources</span><span>Contact Us</span>
  </nav>
</header>

<section class="hero" role="img" aria-label="Doctor in a white coat with stethoscope, arms crossed, in a bright clinic">
  <h1 class="hero-title">Healthcare that works<br>right on time.</h1>
  <p class="hero-text">Pinegate Health Group delivers reliable, patient-centered medical care<br>with seamless online scheduling and modern clinical services.</p>
  <div class="btn" style="left:488px;top:363px;width:224px;height:48px">Book an Appointment</div>
  <div class="dots"><span></span><span class="on"></span><span></span></div>
</section>

<section class="about">
  <div class="abs" style="left:111px;top:820px;width:182px;height:182px;border-radius:50%;background:#e6f3fa"></div>
  <div class="abs" style="left:144px;top:849px;width:452px;height:452px;border-radius:50%;border:3px solid var(--accent)"></div>
  <div class="abs" role="img" aria-label="Nurse helping an older patient at a laptop" style="left:150px;top:851px;width:444px;height:444px;border-radius:50%;background:linear-gradient(135deg,#c9d7e2,#6f93b8 55%,#d8e1ea)"></div>
  <div class="abs" style="left:275px;top:883px;width:22px;height:22px;border-radius:50%;background:var(--white)"></div>
  <div class="abs" role="img" aria-label="Hand holding a glowing medical cross" style="left:430px;top:1120px;width:178px;height:178px;border-radius:50%;border:4px solid var(--white);background:radial-gradient(circle,#9fe0f2,#2b87b6 60%,#123d63)"></div>

  <h2 class="heading abs" style="left:668px;top:866px;font-size:38px">About <span class="hl">Us</span></h2>
  <div class="rule" style="left:668px;top:912px;width:55px"></div>
  <div class="about-text abs" style="left:668px;top:944px;width:421px">
    <p>Pinegate Health Group is a modern medical practice designed to make healthcare simple, efficient, and accessible. Our team provides comprehensive medical services in a calm, professional environment—focused on your time, your health, and your peace of mind. easy online booking to attentive in-office care, we're built to keep your health running smoothly.</p>
    <p>Lorem ipsum dolor sit amet, consectetur adipiscing elit, sed do eiusmod tempor incididunt ut labore et dolore magna aliqua. Ut enim ad minim veniamea.</p>
  </div>
  <div class="btn" style="left:668px;top:1200px;width:146px;height:48px">Learn More</div>
</section>

<section class="services">
  <h2 class="heading abs" style="left:0;width:1200px;top:86px;text-align:center;font-size:38px"><span class="hl">Our</span> Services</h2>
  <div class="rule" style="left:570px;top:134px;width:60px"></div>

  <svg class="arrow" style="left:38px;top:378px" width="40" height="22" viewBox="0 0 40 22"><path d="M39 11H3M12 2L2 11l10 9" stroke="#555" stroke-width="2.5" fill="none"/></svg>
  <svg class="arrow" style="left:1122px;top:378px" width="40" height="22" viewBox="0 0 40 22"><path d="M1 11h36M28 2l10 9-10 9" stroke="#555" stroke-width="2.5" fill="none"/></svg>

  <article class="card" style="left:111px">
    <div class="card-photo" role="img" aria-label="Doctors reviewing notes on a clipboard" style="background:linear-gradient(135deg,#eef1f4,#b9c9d9 60%,#e4e9ee)"></div>
    <div class="card-icon" style="background:var(--blue)"><svg width="38" height="38" viewBox="0 0 38 38" fill="none" stroke="#fff" stroke-width="2"><path d="M19 8c3-4 9-2 9 3s-9 11-9 11-9-6-9-11 6-7 9-3z"/><path d="M6 22l7 8h8M32 22l-7 8h-8"/></svg></div>
    <h3>Primary Care</h3>
    <p>Lorem ipsum dolor sit amet, consectetur adipiscing elit, sed do eiusmod temea.</p>
    <div class="btn btn-ghost">Learn More</div>
  </article>

  <article class="card" style="left:445px">
    <div class="card-photo" role="img" aria-label="Doctor examining a patient's back" style="background:linear-gradient(135deg,#8e9590,#c6c3bd 55%,#e7e6e2)"></div>
    <div class="card-icon" style="background:var(--accent)"><svg width="34" height="38" viewBox="0 0 34 38" fill="none" stroke="#fff" stroke-width="2"><rect x="7" y="4" width="20" height="28" rx="2"/><path d="M11 12h12M11 17h12M11 22h8"/></svg></div>
    <h3>Chronic Condition<br>Management</h3>
    <p>Lorem ipsum dolor sit amet, consectetur adipiscing elit, sed do eiusmod temea.</p>
    <div class="btn">Learn More</div>
  </article>

  <article class="card" style="left:781px">
    <div class="card-photo" role="img" aria-label="Doctor talking with an older patient" style="background:linear-gradient(135deg,#d9dfe4,#a9b6c2 55%,#eef0f2)"></div>
    <div class="card-icon" style="background:var(--blue)"><svg width="36" height="36" viewBox="0 0 36 36" fill="none" stroke="#fff" stroke-width="2"><rect x="5" y="8" width="26" height="22" rx="2"/><path d="M5 14h26M12 5v6M24 5v6M11 19h3M17 19h3M23 19h3M11 24h3M17 24h3"/></svg></div>
    <h3>Wellness Visits</h3>
    <p>Lorem ipsum dolor sit amet, consectetur adipiscing elit, sed do eiusmod temea.</p>
    <div class="btn btn-ghost">Learn More</div>
  </article>
</section>

<section class="booking">
  <div class="abs" role="img" aria-label="Medical worker holding a stethoscope" style="left:0;top:2120px;width:659px;height:532px;background:linear-gradient(120deg,#6aa9cf,#a9cde2 45%,#e8eef2 75%,#d5dde3)"></div>
  <div class="book-box">
    <h2 class="abs" style="left:84px;top:85px;font:700 38px/46px 'Montserrat',Arial,sans-serif;text-transform:uppercase">Book an<br>Appointment</h2>
    <div class="abs" style="left:84px;top:181px;width:55px;height:3px;background:var(--white)"></div>
    <div class="abs" style="left:84px;top:198px;width:421px">
      <p>Scheduling care should be easy. With our secure online booking system, you can request or schedule appointments anytime—no phone calls, no waiting.</p>
      <p>Lorem ipsum dolor sit amet, consectetur adipiscing elit, sed do eiusmod tempor incididunt ut labore et dolore magna aliqua. Ut enim ad minim veniam, quis nostrud exercitation ullamco laboris nisi ut aliquip ex ea commodo consequat.</p>
    </div>
    <div class="btn" style="left:84px;top:401px;width:128px;height:46px">Book Now</div>
  </div>
</section>

<section class="testimonials">
  <h2 class="heading abs" style="left:0;width:1200px;top:2855px;text-align:center;font-size:38px">Testimonials</h2>
  <div class="rule" style="left:570px;top:2902px;width:60px"></div>
  <div class="round-btn" style="left:68px;top:3074px;background:#e8eaed"><svg width="10" height="14" viewBox="0 0 10 14"><path d="M8 1L2 7l6 6" stroke="#222" stroke-width="2" fill="none"/></svg></div>
  <div class="round-btn" style="left:1095px;top:3074px;background:var(--accent)"><svg width="10" height="14" viewBox="0 0 10 14"><path d="M2 1l6 6-6 6" stroke="#fff" stroke-width="2" fill="none"/></svg></div>
  <div class="quote-card">
    <p class="abs" style="left:138px;top:44px;width:520px;font:400 18px/30px 'Roboto',Arial,sans-serif;color:var(--ink)">Lorem ipsum dolor sit amet, consectetur adipiscing elit, sed do eiusmod tempor incididunt ut labore et dolore magna aliqua. Ut enim ad minim veniam, quis nostrud exercitation ullamco laboris nisi ut aliquip ex ea commodo consequat. Duis aute irure dolor in reprehenderit in voluptatea.</p>
    <div class="abs" style="left:138px;top:209px;font:700 21px 'Roboto',Arial,sans-serif;color:var(--ink)">- DANIEL REYES, <span style="font:400 14px 'Roboto',Arial,sans-serif;color:var(--muted)">United States</span></div>
    <svg class="abs" style="left:138px;top:236px" width="84" height="15" viewBox="0 0 84 15"><g fill="#d4906a"><path id="s" d="M7 0l2 5h5l-4 3 2 5-5-3-5 3 2-5-4-3h5z"/><use href="#s" x="17"/><use href="#s" x="34"/><use href="#s" x="51"/><use href="#s" x="68"/></g></svg>
    <svg class="abs" style="left:565px;top:196px" width="90" height="58" viewBox="0 0 90 58"><g fill="#e3e5e8"><circle cx="20" cy="36" r="19"/><path d="M4 34C6 14 18 4 34 2l2 6C24 12 18 20 20 30z"/><circle cx="66" cy="36" r="19"/><path d="M50 34C52 14 64 4 80 2l2 6C70 12 64 20 66 30z"/></g></svg>
  </div>
  <div class="abs" style="left:195px;top:2994px;width:196px;height:196px;border-radius:50%;background:var(--white);box-shadow:0 2px 12px rgba(0,0,0,.12)"></div>
  <div class="abs" role="img" aria-label="Portrait of a smiling customer in a denim shirt" style="left:207px;top:3006px;width:172px;height:172px;border-radius:50%;background:linear-gradient(160deg,#e9ecef,#8fa7c2 60%,#4f6f94)"></div>
</section>

<section class="contact">
  <h2 class="heading abs" style="left:0;width:1200px;top:84px;text-align:center;font-size:38px">Get in <span class="hl">Touch</span></h2>
  <div class="rule" style="left:600px;top:132px;width:60px"></div>

  <div class="info" style="left:220px">
    <svg width="44" height="46" viewBox="0 0 44 46" fill="none" stroke="#d4906a" stroke-width="2"><path d="M22 36S10 24 10 15a12 12 0 0124 0c0 9-12 21-12 21z"/><circle cx="22" cy="15" r="5"/><path d="M6 34l-4 10h40l-4-10"/></svg>
    <div><b>Location:</b><span>465, Lorum Ipsum Dolore Sed,<br>United States</span></div>
  </div>
  <div class="info" style="left:512px">
    <svg width="44" height="44" viewBox="0 0 44 44" fill="none" stroke="#d4906a" stroke-width="2"><path d="M12 4l7 8-4 5c2 5 6 9 11 11l5-4 8 7-5 6C20 37 7 24 5 9z"/><path d="M26 6a12 12 0 0112 12M26 12a6 6 0 016 6"/></svg>
    <div><b>Phone:</b><span>+1 (555) 014 2200</span></div>
  </div>
  <div class="info" style="left:730px">
    <svg width="46" height="44" viewBox="0 0 46 44" fill="none" stroke="#d4906a" stroke-width="2"><rect x="3" y="10" width="22" height="30"/><rect x="13" y="4" width="22" height="30"/><rect x="23" y="12" width="20" height="28"/><path d="M27 20h12M27 26h12M27 32h8"/></svg>
    <div><b>Email:</b><span>info@pinegatehealth.com</span></div>
  </div>

  <label class="field-label" style="left:147px;top:236px">First Name:</label>
  <div class="field" style="left:147px;top:262px;width:434px">Enter Your First Name</div>
  <label class="field-label" style="left:618px;top:236px">Last Name:</label>
  <div class="field" style="left:618px;top:262px;width:435px">Enter Your Last Name</div>
  <label class="field-label" style="left:147px;top:329px">Phone:</label>
  <div class="field" style="left:147px;top:355px;width:434px">Enter Phone Number</div>
  <label class="field-label" style="left:618px;top:329px">Email:</label>
  <div class="field" style="left:618px;top:355px;width:435px">Enter Email Address</div>
  <label class="field-label" style="left:147px;top:422px">Message</label>
  <div class="field" style="left:147px;top:449px;width:906px;height:87px">Enter Comments</div>
  <div class="btn" style="left:515px;top:558px;width:170px;height:47px">Send Message</div>
</section>

<footer class="site-footer">
  <div class="abs" style="left:111px;top:141px;font:700 28px/37px 'Montserrat',Arial,sans-serif;text-transform:uppercase">Pinegate<br>Health Group</div>

  <h4 style="left:371px">Contact Us</h4>
  <div class="foot-item" style="top:109px"><i><svg width="14" height="18" viewBox="0 0 14 18"><path d="M7 17S1 10 1 6a6 6 0 0112 0c0 4-6 11-6 11z" fill="#d4906a"/><circle cx="7" cy="6" r="2" fill="#fff"/></svg></i><span>465, Lorum Ipsum Dolore Sed,<br>United States</span></div>
  <div class="foot-item" style="top:169px"><i><svg width="16" height="16" viewBox="0 0 16 16"><path d="M4 1l3 3-2 2c1 2 3 4 5 5l2-2 3 3-2 3C7 15 1 9 1 3z" fill="#d4906a"/></svg></i><span>Call Us:<br>+1 (555) 014 2200</span></div>
  <div class="foot-item" style="top:229px"><i><svg width="16" height="12" viewBox="0 0 16 12"><rect width="16" height="12" rx="1" fill="#d4906a"/><path d="M1 1l7 6 7-6" stroke="#fff" stroke-width="1.5" fill="none"/></svg></i><span>Email Us:<br>info@pinegatehealth.com</span></div>

  <h4 style="left:659px">Quick Links</h4>
  <ul class="quick"><li>Home</li><li>About Us</li><li>Services</li><li>Providers</li><li>Patient Resources</li><li>Contact Us</li></ul>

  <h4 style="left:829px">Newsletter</h4>
  <div class="abs" style="left:830px;top:118px;width:259px;height:46px;background:var(--white);padding:15px 18px;font:400 13px 'Roboto',Arial,sans-serif;color:#666">Email Address</div>
  <svg class="abs" style="left:1055px;top:133px" width="16" height="16" viewBox="0 0 16 16"><path d="M15 1L1 7l5 2 2 6z" fill="#d4906a"/></svg>
  <div class="social" aria-label="Social media links"><span class="on"></span><span></span><span></span><span></span></div>

  <div class="abs" style="left:0;top:304px;width:1200px;height:1px;background:rgba(255,255,255,.15)"></div>
  <div class="abs" style="left:0;width:1200px;top:326px;text-align:center;font:400 12px 'Roboto',Arial,sans-serif">© 2026 <b>PINEGATE HEALTH GROUP</b> &nbsp;/&nbsp; Disclaimer &nbsp;/&nbsp; Privacy</div>
</footer>

</body>
</html>
```